Custom Office Whiteboard for Staff

I need a custom whiteboard layout design. All fields are contained in the attached images along with artwork requirements including required bleed. Size will be 1200mm x 900mm.

Feel free to make is more visually appealing than this draft.

Use colors blue, black and white to keep company feel.

Font styles to use
Sans Serif

Colors
ffffff
000000
33a6d7

```html
<!DOCTYPE html>
<html lang="en">
<head>
<meta charset="utf-8">
<title>Skyward Ballooning – Staff Whiteboard</title>
<link rel="stylesheet" href="https://fonts.googleapis.com/css2?family=Mulish:wght@400;500;600;700&display=swap">
<style>
  :root {
    --blue: #0aacea;
    --dark: #4a4a4a;
    --black: #111111;
    --white: #ffffff;
    --line: #d4d4d4;
    --backdrop: #5c5c5c;
  }
  * { box-sizing: border-box; margin: 0; padding: 0; }
  html, body { width: 1200px; height: 957px; overflow: hidden; }
  body { background: var(--backdrop); font-family: "Mulish", sans-serif; color: var(--black); position: relative; }

  .board { position: absolute; left: 50px; top: 57px; width: 1100px; height: 844px; background: var(--white); }
  .crop { position: absolute; width: 35px; height: 35px; border-color: #222; border-style: solid; border-width: 0; }
  .crop.tl { left: 0; top: 0; border-right-width: 1px; border-bottom-width: 1px; }
  .crop.tr { right: 0; top: 0; border-left-width: 1px; border-bottom-width: 1px; }
  .crop.bl { left: 0; bottom: 0; border-right-width: 1px; border-top-width: 1px; }
  .crop.br { right: 0; bottom: 0; border-left-width: 1px; border-top-width: 1px; }

  .brand { position: absolute; left: 118px; top: 120px; width: 320px; display: flex; align-items: center; gap: 10px; white-space: nowrap; }
  .brand-dot { flex: none; width: 18px; height: 18px; border-radius: 50%; background: var(--blue); }
  .brand-name { font-size: 26px; font-weight: 700; color: var(--black); }

  .contact { position: absolute; left: 475px; top: 100px; list-style: none; }
  .contact li { display: flex; align-items: center; gap: 9px; height: 27.5px; font-size: 16px; white-space: nowrap; }
  .contact svg { flex: none; width: 16px; height: 16px; }

  .company { position: absolute; left: 793px; top: 102px; font-size: 16px; line-height: 1.2; white-space: nowrap; }
  .company p + p.gap { margin-top: 5px; }

  .panel { position: absolute; }
  .panel table { width: 100%; border-collapse: collapse; table-layout: fixed; }
  .panel-title { background: var(--blue); color: var(--white); text-align: center; font-weight: 500; }
  .panel th { background: var(--dark); color: var(--white); font-weight: 500; font-size: 11px; line-height: 1.05; border-right: 1px solid #5d5d5d; }
  .panel td { border: 1px solid var(--line); font-size: 9px; text-align: center; }

  .crew { left: 88px; top: 204px; width: 720px; }
  .crew .panel-title { height: 32px; line-height: 32px; font-size: 19px; }
  .crew th { height: 29px; }
  .crew td { height: 24.1px; }

  .notes { position: absolute; left: 820px; top: 204px; width: 191px; height: 350px; border: 2px solid var(--line); border-top: none; border-radius: 0 0 4px 4px; }
  .notes-title { position: relative; background: var(--blue); color: var(--white); height: 46px; line-height: 46px; text-align: center; font-size: 25px; font-weight: 500; margin: 0 -2px; }
  .notes-title::after { content: ""; position: absolute; left: 50%; bottom: -9px; margin-left: -10px; border: 10px solid transparent; border-bottom: 0; border-top-color: var(--blue); }

  .sched .panel-title { height: 24px; line-height: 24px; font-size: 13px; }
  .sched th { height: 19px; font-size: 11px; }
  .sched td { height: 19.6px; }
  .six { left: 88px; top: 559px; width: 232px; }
  .twelve { left: 325px; top: 559px; width: 232px; }
  .fleet { left: 563px; top: 559px; width: 448px; }
</style>
</head>
<body>
<main class="board">
  <span class="crop tl"></span><span class="crop tr"></span><span class="crop bl"></span><span class="crop br"></span>

  <div class="brand"><span class="brand-dot"></span><span class="brand-name">Skyward Ballooning</span></div>

  <ul class="contact">
    <li><svg viewBox="0 0 16 16"><rect x="1.5" y="3.5" width="13" height="9" fill="none" stroke="#0aacea" stroke-width="1.2"/><path d="M1.5 3.5 8 9l6.5-5.5" fill="none" stroke="#0aacea" stroke-width="1.2"/></svg>hello@skywardballooning.example</li>
    <li><svg viewBox="0 0 16 16"><circle cx="8" cy="8" r="6.5" fill="none" stroke="#0aacea" stroke-width="1.2"/><ellipse cx="8" cy="8" rx="3" ry="6.5" fill="none" stroke="#0aacea" stroke-width="1.2"/><path d="M1.5 8h13M2.5 5h11M2.5 11h11" stroke="#0aacea" stroke-width="1"/></svg>www.skywardballooning.example</li>
    <li><svg viewBox="0 0 16 16"><circle cx="8" cy="8" r="7" fill="none" stroke="#0aacea" stroke-width="1.2"/><path d="M5.5 4.5c-1 1 0 3.5 2 5.5s4.5 3 5.5 2l-1.5-1.8-1.5.8c-1-.5-2.2-1.7-2.7-2.7l.8-1.5z" fill="#0aacea"/></svg>1300 555 019</li>
  </ul>

  <div class="company">
    <p>Highwind Aerostats Pty Ltd</p>
    <p>T/A Skyward Ballooning</p>
    <p class="gap">CASA AOC: S900114</p>
    <p class="gap">Certificate of Approval: 5186</p>
  </div>

  <section class="panel crew">
    <div class="panel-title">FLIGHT / GROUND CREW</div>
    <table>
      <thead><tr><th>Crew Name</th><th>License Class</th><th>Medical</th><th>BFR</th><th>Instructor<br>Rating</th><th>CAO 20.11</th><th>DAMP</th><th>Maintenance<br>Authority</th><th>ASIC</th></tr></thead>
      <tbody>
        <tr><td></td><td></td><td></td><td></td><td></td><td></td><td></td><td></td><td></td></tr>
        <tr><td></td><td></td><td></td><td></td><td></td><td></td><td></td><td></td><td></td></tr>
        <tr><td></td><td></td><td></td><td></td><td></td><td></td><td></td><td></td><td></td></tr>
        <tr><td></td><td></td><td></td><td></td><td></td><td></td><td></td><td></td><td></td></tr>
        <tr><td></td><td></td><td></td><td></td><td></td><td></td><td></td><td></td><td></td></tr>
        <tr><td></td><td></td><td></td><td></td><td></td><td></td><td></td><td></td><td></td></tr>
        <tr><td></td><td></td><td></td><td></td><td></td><td></td><td></td><td></td><td></td></tr>
        <tr><td></td><td></td><td></td><td></td><td></td><td></td><td></td><td></td><td></td></tr>
        <tr><td></td><td></td><td></td><td></td><td></td><td></td><td></td><td></td><td></td></tr>
        <tr><td></td><td></td><td></td><td></td><td></td><td></td><td></td><td></td><td></td></tr>
        <tr><td></td><td></td><td></td><td></td><td></td><td></td><td></td><td></td><td></td></tr>
        <tr><td></td><td></td><td></td><td></td><td></td><td></td><td></td><td></td><td></td></tr>
      </tbody>
    </table>
  </section>

  <aside class="notes"><div class="notes-title">NOTES</div></aside>

  <section class="panel sched six">
    <div class="panel-title">6 MONTHLY TASKS</div>
    <table>
      <colgroup><col style="width:58%"><col></colgroup>
      <thead><tr><th>Task</th><th>Due Date</th></tr></thead>
      <tbody>
        <tr><td>Operations Manual</td><td></td></tr>
        <tr><td>Staff Meeting</td><td></td></tr>
        <tr><td>SMS Meeting</td><td></td></tr>
        <tr><td>Fire Extinguisher Inspection</td><td></td></tr>
        <tr><td>Flight Instrument Inspection</td><td></td></tr>
        <tr><td></td><td></td></tr>
        <tr><td></td><td></td></tr>
        <tr><td></td><td></td></tr>
      </tbody>
    </table>
  </section>

  <section class="panel sched twelve">
    <div class="panel-title">12 MONTHLY TASKS</div>
    <table>
      <colgroup><col style="width:50%"><col></colgroup>
      <thead><tr><th>Task</th><th>Due Date</th></tr></thead>
      <tbody>
        <tr><td>CofA Internal Audit</td><td></td></tr>
        <tr><td>SMS Audit</td><td></td></tr>
        <tr><td>Fatigue Training</td><td></td></tr>
        <tr><td>CAO 20.11</td><td></td></tr>
        <tr><td></td><td></td></tr>
        <tr><td></td><td></td></tr>
        <tr><td></td><td></td></tr>
        <tr><td></td><td></td></tr>
      </tbody>
    </table>
  </section>

  <section class="panel sched fleet">
    <div class="panel-title">BALLOON ANNUAL / PERIODIC SCHEDULE</div>
    <table>
      <thead><tr><th>Balloon</th><th>Type</th><th>Annual Date</th><th>Periodic Time</th></tr></thead>
      <tbody>
        <tr><td>VH-KTA</td><td>Ark D90</td><td></td><td></td></tr>
        <tr><td>VH-KTB</td><td>Ark E180</td><td></td><td></td></tr>
        <tr><td>VH-KTC</td><td>Ark E240</td><td></td><td></td></tr>
        <tr><td>VH-KTD</td><td>Ark B400</td><td></td><td></td></tr>
        <tr><td>VH-KTE</td><td>Ark G450</td><td></td><td></td></tr>
        <tr><td></td><td></td><td></td><td></td></tr>
        <tr><td></td><td></td><td></td><td></td></tr>
        <tr><td></td><td></td><td></td><td></td></tr>
      </tbody>
    </table>
  </section>
</main>
</body>
</html>
```